ESL Teacher Training School needs an image designed for website and Social Media use

We need an image designed to promote the Freebies that come our Australian Government accredited, online TESOL Training programme. The image will be added to the landing page of our website (www.qorlinteach.edu.vn) and used in Social Media posts.

What's the key text?

Freebies with your online TESOL Course

- do the practical part in Vietnam or Cambodia
- 9 nights hotel accommodation in Vietnam or Cambodia
- hands-on job support in Vietnam or Cambodia

The colour scheme should be bright and eye catching - red, orange, blue, yellow, light green.....

We'd like to incorporate our logo (attached) and our website address

At the bottom in small print, we must incorporate the following text (small print): Australian RTO: 81926, Course: 52418NAT

The final design should communicate - fun, adventure, adventure abroad
Updates

there are a couple of designs that are pretty close to what I'm looking for

Target Market(s)

21 to 45 years of age, males & females, native English speakers

Colors
59FF00
82FF00
B8FF75
E3FFCB
F4FFEA
FFF300
FFF600
FEFA6F
FFFEC7
FFFEE8
EB3D1F
EC4F4E
F09395
F8D3D4
FCEDEE

Requirements
Must have
• simplicity, highlight freebies and what they are
Should not have
• clutter

```html
<!DOCTYPE html>
<html lang="en">
<head>
<meta charset="utf-8">
<title>Freebies with your online TESOL course</title>
<link rel="stylesheet" href="https://fonts.googleapis.com/css2?family=Anton&family=Poppins:wght@400;500;600;700;800&display=swap">
<style>
  :root {
    --sheet: #dcdcdc;
    --amber: #f9b70f;
    --amber-deep: #f08c10;
    --rust: #e0500a;
    --red: #c80000;
    --red-bright: #eb3d1f;
    --ink: #333333;
    --blue: #0840c8;
    --white: #ffffff;
    --cream: #ffe9b0;
    --brown: #5a3a10;
    --hoodie: #1b6fe0;
    --leaf: #10b46a;
  }
  html, body {
    margin: 0;
    padding: 0;
    width: 839px;
    height: 1200px;
    overflow: hidden;
    background: var(--sheet);
  }
  .sheet {
    position: relative;
    width: 839px;
    height: 1200px;
  }
  .banner { position: absolute; display: block; }
  .banner--square { left: 75px; top: 59px; }
  .banner--wide { left: 35px; top: 793px; }
  .headline-free { font-family: "Anton", Impact, sans-serif; }
  .sub-line { font-family: "Poppins", Arial, sans-serif; font-weight: 500; }
  .course-line { font-family: "Poppins", Arial, sans-serif; font-weight: 800; }
  .perk-text { font-family: "Poppins", Arial, sans-serif; font-weight: 500; fill: var(--white); }
  .brand-name { font-family: "Poppins", Arial, sans-serif; font-weight: 500; letter-spacing: 2px; }
  .site-url { font-family: "Poppins", Arial, sans-serif; font-weight: 700; fill: var(--white); }
  .small-print { font-family: "Poppins", Arial, sans-serif; font-weight: 400; }
  .icon-line { fill: none; stroke: var(--blue); stroke-width: 1.6; stroke-linejoin: round; stroke-linecap: round; }
</style>
</head>
<body>
<main class="sheet">

  <!-- Square social post -->
  <svg class="banner banner--square" width="679" height="679" viewBox="0 0 679 679" xmlns="http://www.w3.org/2000/svg">
    <defs>
      <linearGradient id="sq-backdrop" x1="0" y1="0" x2="1" y2="1">
        <stop offset="0" stop-color="var(--amber-deep)"/>
        <stop offset="0.45" stop-color="var(--amber)"/>
        <stop offset="1" stop-color="var(--amber-deep)"/>
      </linearGradient>
      <linearGradient id="sq-perk-bar" x1="0" y1="0" x2="1" y2="0">
        <stop offset="0" stop-color="var(--rust)"/>
        <stop offset="1" stop-color="var(--amber-deep)" stop-opacity="0.55"/>
      </linearGradient>
      <linearGradient id="sq-figure" x1="0" y1="0" x2="0" y2="1">
        <stop offset="0" stop-color="var(--hoodie)"/>
        <stop offset="0.55" stop-color="var(--leaf)"/>
        <stop offset="1" stop-color="var(--ink)"/>
      </linearGradient>
      <linearGradient id="sq-horn" x1="0" y1="0" x2="1" y2="0">
        <stop offset="0" stop-color="#a80000"/>
        <stop offset="1" stop-color="var(--red-bright)"/>
      </linearGradient>
    </defs>

    <rect class="backdrop" width="679" height="679" fill="url(#sq-backdrop)"/>
    <path class="speech-bubble" d="M197 0 C150 60 110 130 70 200 L112 296 C170 300 220 285 280 275 C360 260 420 240 500 250 C580 260 620 245 679 228 L679 0 Z" fill="var(--white)"/>

    <rect class="megaphone" x="0" y="197" width="119" height="141" rx="10" fill="url(#sq-horn)" role="img" aria-label="Illustration of a red megaphone"/>

    <g class="headline">
      <text class="headline-free" x="200" y="145" font-size="160" textLength="460" lengthAdjust="spacingAndGlyphs" transform="skewX(-8)">
        <tspan fill="var(--red)">FREE</tspan><tspan fill="var(--ink)">BIES</tspan>
      </text>
      <text class="sub-line" x="181" y="171" font-size="29" fill="var(--ink)" textLength="452" lengthAdjust="spacing">WITH YOUR ONLINE</text>
      <text class="course-line" x="180" y="227" font-size="64" fill="var(--blue)" textLength="460" lengthAdjust="spacingAndGlyphs">TESOL COURSE</text>
    </g>

    <rect class="student-figure" x="14" y="257" width="272" height="405" rx="40" fill="url(#sq-figure)" role="img" aria-label="Illustration of a student with a headset studying on a laptop in a bean bag chair"/>

    <g class="perk">
      <rect x="311" y="300" width="368" height="57" fill="url(#sq-perk-bar)"/>
      <circle cx="311" cy="329" r="30" fill="var(--white)" stroke="var(--red)" stroke-width="4"/>
      <g class="icon-line" transform="translate(311 329)">
        <rect x="-15" y="-14" width="30" height="19" rx="2"/>
        <path d="M-2 -9 L5 -4.5 L-2 0 Z"/>
        <circle cx="-9" cy="10" r="2.2"/><circle cx="0" cy="10" r="2.2"/><circle cx="9" cy="10" r="2.2"/>
      </g>
      <text class="perk-text" x="349" y="325" font-size="17">Do the practical part in</text>
      <text class="perk-text" x="349" y="347" font-size="17">Vietnam or Cambodia</text>
    </g>

    <g class="perk">
      <rect x="311" y="388" width="368" height="57" fill="url(#sq-perk-bar)"/>
      <circle cx="311" cy="417" r="30" fill="var(--white)" stroke="var(--red)" stroke-width="4"/>
      <g class="icon-line" transform="translate(311 417)">
        <rect x="-17" y="-4" width="8" height="12" rx="1"/>
        <path d="M-6 8 V-6 H16 V8 M-6 2 H16 M-2 -2 H5 V2 M8 -2 H13 V2"/>
      </g>
      <text class="perk-text" x="349" y="413" font-size="17">9 nights hotel accommodation</text>
      <text class="perk-text" x="349" y="435" font-size="17">in Vietnam or Cambodia</text>
    </g>

    <g class="perk">
      <rect x="311" y="476" width="368" height="57" fill="url(#sq-perk-bar)"/>
      <circle cx="311" cy="505" r="30" fill="var(--white)" stroke="var(--red)" stroke-width="4"/>
      <g class="icon-line" transform="translate(311 505)">
        <rect x="-16" y="-14" width="28" height="24" rx="2"/>
        <path d="M-16 -8 H12"/>
        <circle cx="4" cy="4" r="6"/>
        <path d="M8.5 8.5 L14 14"/>
      </g>
      <text class="perk-text" x="355" y="501" font-size="17">Hands-on job support in</text>
      <text class="perk-text" x="355" y="523" font-size="17">Vietnam or Cambodia</text>
    </g>

    <rect class="footer-rule" x="0" y="562" width="679" height="8" fill="var(--ink)"/>
    <rect class="footer-band" x="0" y="570" width="679" height="109" fill="var(--red)"/>
    <rect class="student-seat-overlap" x="14" y="570" width="272" height="92" rx="30" fill="var(--ink)" role="img" aria-label="Bean bag chair of the student illustration"/>

    <g class="brand">
      <circle cx="362" cy="612" r="22" fill="var(--white)"/>
      <text class="brand-name" x="362" y="661" font-size="14" fill="var(--white)" text-anchor="middle">QORLIN TEACH</text>
    </g>

    <rect class="url-box" x="431" y="591" width="248" height="35" fill="var(--ink)"/>
    <text class="site-url" x="442" y="616" font-size="20" textLength="215" lengthAdjust="spacingAndGlyphs">www.qorlinteach.edu.vn</text>
    <text class="small-print" x="435" y="646" font-size="13" fill="var(--cream)">Australian RTO: 81926,</text>
    <text class="small-print" x="435" y="662" font-size="13" fill="var(--cream)">Course: 52418NAT</text>
  </svg>

  <!-- Wide web banner -->
  <svg class="banner banner--wide" width="758" height="325" viewBox="0 0 758 325" xmlns="http://www.w3.org/2000/svg">
    <defs>
      <linearGradient id="wd-backdrop" x1="0" y1="0" x2="1" y2="1">
        <stop offset="0" stop-color="var(--amber)"/>
        <stop offset="0.6" stop-color="var(--amber)"/>
        <stop offset="1" stop-color="var(--amber-deep)"/>
      </linearGradient>
      <linearGradient id="wd-perk-bar" x1="0" y1="0" x2="1" y2="0">
        <stop offset="0" stop-color="var(--rust)"/>
        <stop offset="1" stop-color="var(--amber-deep)" stop-opacity="0.4"/>
      </linearGradient>
      <linearGradient id="wd-figure" x1="0" y1="0" x2="0" y2="1">
        <stop offset="0" stop-color="var(--hoodie)"/>
        <stop offset="0.55" stop-color="var(--leaf)"/>
        <stop offset="1" stop-color="var(--ink)"/>
      </linearGradient>
      <linearGradient id="wd-horn" x1="0" y1="0" x2="1" y2="0">
        <stop offset="0" stop-color="#a80000"/>
        <stop offset="1" stop-color="var(--red-bright)"/>
      </linearGradient>
    </defs>

    <rect class="backdrop" width="758" height="325" fill="url(#wd-backdrop)"/>
    <path class="speech-bubble" d="M163 0 C140 50 125 100 100 140 L108 225 C200 205 260 215 330 222 C420 230 520 215 600 195 C640 180 665 120 660 60 L690 0 Z" fill="var(--white)"/>

    <g class="brand">
      <circle cx="60" cy="36" r="18" fill="var(--red)"/>
      <text class="brand-name" x="60" y="70" font-size="10" fill="var(--red)" text-anchor="middle">QORLIN TEACH</text>
    </g>

    <rect class="megaphone" x="0" y="137" width="106" height="110" rx="10" fill="url(#wd-horn)" role="img" aria-label="Illustration of a red megaphone"/>

    <g class="headline">
      <text class="headline-free" x="182" y="111" font-size="122" textLength="410" lengthAdjust="spacingAndGlyphs" transform="skewX(-8)">
        <tspan fill="var(--red)">FREE</tspan><tspan fill="var(--ink)">BIES</tspan>
      </text>
      <text class="sub-line" x="168" y="136" font-size="23" fill="var(--ink)" textLength="351" lengthAdjust="spacing">WITH YOUR ONLINE</text>
      <text class="course-line" x="168" y="176" font-size="48" fill="var(--blue)" textLength="359" lengthAdjust="spacingAndGlyphs">TESOL COURSE</text>
    </g>

    <rect class="student-figure" x="590" y="4" width="165" height="227" rx="30" fill="url(#wd-figure)" role="img" aria-label="Illustration of a student with a headset studying on a laptop in a bean bag chair"/>

    <g class="perk">
      <rect x="69" y="257" width="196" height="34" fill="url(#wd-perk-bar)"/>
      <circle cx="69" cy="274" r="18" fill="var(--white)" stroke="var(--red)" stroke-width="2.5"/>
      <g class="icon-line" transform="translate(69 274) scale(0.6)">
        <rect x="-15" y="-14" width="30" height="19" rx="2"/>
        <path d="M-2 -9 L5 -4.5 L-2 0 Z"/>
        <circle cx="-9" cy="10" r="2.2"/><circle cx="0" cy="10" r="2.2"/><circle cx="9" cy="10" r="2.2"/>
      </g>
      <text class="perk-text" x="91" y="271" font-size="11">Do the practical part in</text>
      <text class="perk-text" x="91" y="284" font-size="11">Vietnam or Cambodia</text>
    </g>

    <g class="perk">
      <rect x="289" y="257" width="216" height="34" fill="url(#wd-perk-bar)"/>
      <circle cx="289" cy="274" r="18" fill="var(--white)" stroke="var(--red)" stroke-width="2.5"/>
      <g class="icon-line" transform="translate(289 274) scale(0.6)">
        <rect x="-17" y="-4" width="8" height="12" rx="1"/>
        <path d="M-6 8 V-6 H16 V8 M-6 2 H16 M-2 -2 H5 V2 M8 -2 H13 V2"/>
      </g>
      <text class="perk-text" x="312" y="271" font-size="11">9 nights hotel accommodation</text>
      <text class="perk-text" x="312" y="284" font-size="11">in Vietnam or Cambodia</text>
    </g>

    <g class="perk">
      <rect x="522" y="257" width="188" height="34" fill="url(#wd-perk-bar)"/>
      <circle cx="522" cy="274" r="18" fill="var(--white)" stroke="var(--red)" stroke-width="2.5"/>
      <g class="icon-line" transform="translate(522 274) scale(0.6)">
        <rect x="-16" y="-14" width="28" height="24" rx="2"/>
        <path d="M-16 -8 H12"/>
        <circle cx="4" cy="4" r="6"/>
        <path d="M8.5 8.5 L14 14"/>
      </g>
      <text class="perk-text" x="549" y="269" font-size="11">Hands-on job support in</text>
      <text class="perk-text" x="549" y="282" font-size="11">Vietnam or Cambodia</text>
    </g>

    <text class="small-print" x="371" y="308" font-size="11" fill="var(--brown)" text-anchor="middle">Australian RTO: 81926, Course: 52418NAT</text>
  </svg>

</main>
</body>
</html>
```